Zielgruppe
Zielgruppe sind Großhändler in der Elektrotechnik, Fachfirmen für Notbeleuchtung. Produkte: Notbeleuchtungssysteme, Not- und Sicherheitsleuchten, Akkumulatoren/Batterien (industrielle)
Aufgabenstellung
Optimale Darstellung des Logos und der Werte des Unternehmens. Einhaltung der Farben des Logos. Eher eine helle Businesskarte, nicht zu Dunkel.
Wir bitten, dass uns der Gewinner gleich für die ersten 6 Mitarbeiter, welche Visitenkarten in unserem Unternehmen benötigen, zu erstellen.
Die bestehende Visitenkarte kam leider nicht gut an. Falsche Farben und kein komplett abgestimmtes Design.
Die neue Visitenkarte soll gut zur Website passen und die Firma optimal repräsentieren.
!Bitte nicht die Farbe der bestehenden Visitenkarte benutzen sondern nur Farbtöne des Logos. Bitte nicht zwingend am bestehenden Design der Visitenkarte orientieren, wir möchten frische Ideen!

```html
<!DOCTYPE html>
<html lang="de">
<head>
<meta charset="utf-8">
<title>Veltra Systems – Visitenkarte</title>
<link href="https://fonts.googleapis.com/css2?family=Jost:ital,wght@0,400;0,500;1,400&family=Montserrat:wght@700&family=Doto:wght@700&display=swap" rel="stylesheet">
<style>
  :root {
    --magenta: #ab0d5f;
    --slate: #5d6770;
    --stage: #eeeeee;
    --blush: #f0cfdd;
    --paper: #ffffff;
  }
  * { margin: 0; padding: 0; box-sizing: border-box; }
  html, body { width: 826px; height: 1200px; overflow: hidden; background: var(--stage); }
  .canvas { position: relative; width: 826px; height: 1200px; }
  .card {
    position: absolute; left: 83px; width: 660px; height: 386px; overflow: hidden;
    box-shadow: 0 10px 24px rgba(0,0,0,0.12);
  }
  .card-front {
    top: 174px;
    background:
      radial-gradient(ellipse 55% 60% at 8% 8%, var(--blush), transparent 70%),
      radial-gradient(ellipse 45% 40% at 92% 85%, #f2d6e2, transparent 70%),
      radial-gradient(ellipse 50% 45% at 45% 55%, #f5e1ea, transparent 70%),
      var(--paper);
  }
  .card-back { top: 640px; background: var(--magenta); }

  .person { position: absolute; left: 64px; top: 58px; color: var(--magenta); }
  .person-name { font: 700 28px/1 "Montserrat", sans-serif; letter-spacing: -0.3px; }
  .person-role { font: italic 400 13px/15px "Jost", sans-serif; margin-top: 3px; }

  .wordmark {
    position: absolute; display: flex; align-items: center; gap: 9px;
    font-family: "Jost", sans-serif; font-weight: 400; letter-spacing: 1.5px;
  }
  .card-front .wordmark { left: 396px; top: 62px; color: var(--slate); font-size: 21px; }
  .card-back .wordmark { left: 50%; top: 50%; transform: translate(-50%, -50%); color: var(--paper); font-size: 30px; }
  .wordmark-square { display: block; border: 3px solid currentColor; }
  .card-front .wordmark-square { width: 22px; height: 22px; }
  .card-back .wordmark-square { width: 30px; height: 30px; border-width: 4px; }

  .contact { position: absolute; left: 73px; top: 232px; list-style: none; color: var(--slate); font: 400 13.5px/1 "Jost", sans-serif; }
  .contact li { display: flex; align-items: center; gap: 17px; height: 30px; }
  .contact svg { width: 17px; height: 17px; flex: none; }

  .address { position: absolute; left: 397px; top: 236px; color: var(--slate); font: 400 19px/25px "Jost", sans-serif; font-style: normal; }

  .web-strip { position: absolute; left: 0; bottom: 0; width: 660px; height: 40px; }
  .web-strip text { font: 700 44px "Doto", monospace; fill: var(--magenta); opacity: 0.75; }
</style>
</head>
<body>
<main class="canvas">
  <section class="card card-front" aria-label="Vorderseite">
    <div class="person">
      <p class="person-name">Lutz Bramer</p>
      <p class="person-role">Gescaftsfuhrer<br>Managing Director</p>
    </div>

    <div class="wordmark"><span class="wordmark-square"></span>VELTRA SYSTEMS</div>

    <ul class="contact">
      <li>
        <svg viewBox="0 0 20 20" aria-hidden="true"><circle cx="10" cy="10" r="10" fill="#5d6770"/><path d="M6.4 5.2l1.9-.4 1.1 2.6-1.3 1a6.5 6.5 0 0 0 3.5 3.5l1-1.3 2.6 1.1-.4 1.9c-4.7.4-8.8-3.7-8.4-8.4z" fill="#fff"/></svg>
        08731 46120 58
      </li>
      <li>
        <svg viewBox="0 0 20 20" aria-hidden="true"><circle cx="10" cy="10" r="10" fill="#5d6770"/><path d="M6.4 5.2l1.9-.4 1.1 2.6-1.3 1a6.5 6.5 0 0 0 3.5 3.5l1-1.3 2.6 1.1-.4 1.9c-4.7.4-8.8-3.7-8.4-8.4z" fill="#fff"/></svg>
        0172-6839204
      </li>
      <li>
        <svg viewBox="0 0 20 20" aria-hidden="true"><circle cx="10" cy="10" r="10" fill="#5d6770"/><rect x="5" y="6.5" width="10" height="7" rx="1" fill="none" stroke="#fff" stroke-width="1.2"/><path d="M5.3 7l4.7 3.6L14.7 7" fill="none" stroke="#fff" stroke-width="1.2"/></svg>
        lutz.bramer@veltra-systems.com
      </li>
    </ul>

    <address class="address">Veltra Systems GmbH<br>Lindenweg 4<br>D-84028 Landshut</address>

    <svg class="web-strip" viewBox="0 0 660 40" aria-label="www.veltra-systems.com">
      <text x="0" y="37" textLength="660" lengthAdjust="spacingAndGlyphs">WWW.VELTRA-SYSTEMS.COM</text>
    </svg>
  </section>

  <section class="card card-back" aria-label="Rückseite">
    <div class="wordmark"><span class="wordmark-square"></span>VELTRA SYSTEMS</div>
  </section>
</main>
</body>
</html>
```